Yoga Studio Postcard Advertising Flyer

Need a postcard size flyer that will promote our business. The objective is to promote location and availability. Want it to be personal. The objective to connect the audience to the purpose of yoga and the focus on enabling functional well-being. Something that is a very big focus at this point in time in the world. I really want people to see the value in connecting with us via our website, calmora app, pagewell or vibro. The colours are to be bright but not overwhelming and aligned to the logo colours. Its also important to have the location picture on the flyer - unless you think that it is way too much (try a with or without). I don't want this to be a specials brochure - it is an introduction to our brand and our business. No need to over do it with promotional lines apart from come and join us.

Delayed in organising this.

Local yogis and residence who are or want to be focused on well-being.

• Pictures - would have the logo on one side.
• Modern and aligned to website design.

```html
<!DOCTYPE html>
<html lang="en">
<head>
<meta charset="utf-8">
<title>Lantern Reed Yoga – Postcard Flyers</title>
<link rel="stylesheet" href="https://fonts.googleapis.com/css2?family=Archivo:wght@300;400;700;900&display=swap">
<style>
:root{
  --sky:#20a3dd;
  --navy:#0f1b3d;
  --ink:#111111;
  --bar:#efefef;
  --white:#ffffff;
  --photo-wall:#cdbfae;
  --photo-floor:#7a3b1c;
  --photo-glow:#e07a2a;
}
*{box-sizing:border-box;margin:0;padding:0}
html,body{width:1049px;height:1200px;overflow:hidden;background:var(--white);font-family:"Archivo",Arial,sans-serif}
.postcard{position:absolute;left:182px;width:690px;height:418px;background:var(--white);overflow:hidden;box-shadow:0 4px 14px rgba(0,0,0,.22)}
.postcard--side{top:210px}
.postcard--centre{top:651px}
.scene{position:absolute;left:0;top:0;width:690px;height:418px}
.band-top{position:absolute;left:0;top:0;width:470px;height:56px;background:var(--sky);color:var(--white);font-weight:900;font-size:27px;line-height:56px;text-align:center;padding-right:60px}
.brand{position:absolute;color:var(--navy);font-weight:400;text-align:center;white-space:nowrap}
.brand__mark{display:block;width:52px;height:52px;margin:0 auto;border:2px solid var(--sky);border-radius:50%}
.brand__name{display:block;font-size:18px;line-height:20px;letter-spacing:.3px}
.brand__sub{display:block;font-size:11px;line-height:14px;letter-spacing:4px;padding-left:4px}
.headline{position:absolute;color:var(--sky);font-weight:900;text-transform:uppercase;white-space:nowrap}
.tagline{position:absolute;font-weight:700;font-size:11px;line-height:14px;color:var(--ink);white-space:nowrap}
.body{position:absolute;font-size:12.5px;line-height:15px;color:var(--ink)}
.vision{position:absolute;left:0;width:420px;background:var(--sky);color:var(--white);font-weight:300;font-size:12.5px;line-height:15px}
.join{position:absolute;color:var(--navy);font-weight:900;font-size:27px;line-height:32px;white-space:nowrap}
.links{position:absolute;left:0;top:347px;width:420px;height:47px;background:var(--bar)}
.links__globe{position:absolute;left:22px;top:12px}
.links__web{position:absolute;left:52px;top:0;line-height:47px;font-weight:700;font-size:12.5px;color:var(--ink);letter-spacing:.3px}
.social{position:absolute;top:0;line-height:47px;display:flex;align-items:center;gap:4px;font-size:11px;color:var(--navy)}
.social__dot{width:11px;height:11px;border-radius:50%;background:var(--sky)}
.address{position:absolute;left:0;top:394px;width:690px;height:24px;background:var(--navy);color:var(--white);font-size:12.5px;line-height:24px;padding-left:19px;display:flex;align-items:center;gap:7px}
</style>
</head>
<body>

<section class="postcard postcard--side">
  <div class="band-top">Come join us!</div>

  <div class="brand" style="left:24px;top:66px;width:120px">
    <span class="brand__mark" style="margin-bottom:10px"></span>
    <span class="brand__name">Lantern Reed</span>
    <span class="brand__sub">YOGA</span>
  </div>

  <h1 class="headline" style="left:153px;top:78px;font-size:30px;line-height:28px">Enable<br>Functional<br>Wellbeing</h1>

  <p class="tagline" style="left:19px;top:191px">STRENGTHEN YOUR WELL-BEING THROUGH ADAPTIVE YOGA.</p>
  <p class="body" style="left:19px;top:219px;width:362px">Seek to evolve your mind and body through the challenge of yoga. Perfection is a desire and never an outcome through the practice of yoga.</p>

  <div class="vision" style="top:283px;height:51px;padding:10px 0 0 84px">Our vision is to create an atmosphere that enables<br>inclusiveness of the whole community.</div>

  <svg class="scene" viewBox="0 0 690 418" aria-hidden="true">
    <path d="M463,0H690V418H629C478,400 384,318 384,190C384,110 416,46 463,0Z" fill="var(--sky)"/>
    <path d="M480,0H690V418H660C500,408 393,322 393,195C393,112 428,46 480,0Z" fill="var(--navy)"/>
  </svg>
  <svg class="scene" viewBox="0 0 690 418" role="img" aria-label="Photo of the studio interior: a bright chapel hall with yoga mats on a timber floor lit by stained-glass light">
    <defs>
      <linearGradient id="room1" x1="0" y1="0" x2="0" y2="1">
        <stop offset="0" stop-color="var(--photo-wall)"/>
        <stop offset=".5" stop-color="#b8a894"/>
        <stop offset=".62" stop-color="var(--photo-floor)"/>
        <stop offset=".85" stop-color="var(--photo-glow)"/>
        <stop offset="1" stop-color="#5a2a14"/>
      </linearGradient>
    </defs>
    <path d="M505,0H690V412C530,408 413,322 413,195C413,110 450,44 505,0Z" fill="url(#room1)"/>
  </svg>

  <div class="links">
    <svg class="links__globe" width="23" height="23" viewBox="0 0 24 24" aria-hidden="true"><g fill="none" stroke="var(--navy)" stroke-width="1.4"><circle cx="12" cy="12" r="10.5"/><ellipse cx="12" cy="12" rx="4.5" ry="10.5"/><path d="M1.5 12h21M3 6.5h18M3 17.5h18M12 1.5v21"/></g></svg>
    <span class="links__web">lanternreedyoga.com.au</span>
    <span class="social" style="left:206px"><span class="social__dot"></span>pagewell</span>
    <span class="social" style="left:268px"><span class="social__dot"></span>vibro</span>
    <span class="social" style="left:316px"><span class="social__dot"></span>calmora</span>
  </div>
  <div class="address">
    <svg width="12" height="17" viewBox="0 0 12 17" aria-hidden="true"><path d="M6 16C2 10.5 1 8.5 1 6a5 5 0 0 1 10 0c0 2.5-1 4.5-5 10z" fill="none" stroke="var(--white)" stroke-width="1.3"/></svg>
    The Chapel, 48 Harbour Lane Marrick NSW 2099
  </div>

  <svg class="scene" viewBox="0 0 690 418" role="img" aria-label="Photo of the chapel building exterior under a cloudy sky">
    <defs>
      <linearGradient id="chapel1" x1="0" y1="0" x2="0" y2="1">
        <stop offset="0" stop-color="#8fb4d6"/>
        <stop offset=".45" stop-color="#c9ccd0"/>
        <stop offset=".8" stop-color="#6d6a64"/>
        <stop offset="1" stop-color="#3c4a2e"/>
      </linearGradient>
    </defs>
    <circle cx="463" cy="341" r="67" fill="rgba(255,255,255,.35)"/>
    <circle cx="463" cy="341" r="60" fill="url(#chapel1)" stroke="var(--sky)" stroke-width="2.5"/>
  </svg>
</section>

<section class="postcard postcard--centre">
  <div class="brand" style="left:133px;top:6px;width:140px">
    <span class="brand__mark" style="margin-bottom:6px"></span>
    <span class="brand__name">Lantern Reed</span>
    <span class="brand__sub">YOGA</span>
  </div>

  <h2 class="headline" style="left:0;top:116px;width:406px;text-align:center;font-size:26px;line-height:24px">Enable Functional<br>Wellbeing</h2>

  <p class="tagline" style="left:0;top:171px;width:406px;text-align:center">STRENGTHEN YOUR WELL-BEING THROUGH ADAPTIVE YOGA.</p>
  <p class="body" style="left:18px;top:199px;width:362px;text-align:center">Seek to evolve your mind and body through the challenge of yoga. Perfection is a desire and never an outcome through the practice of yoga.</p>

  <div class="vision" style="top:255px;height:37px;padding-top:4px;padding-right:16px;text-align:center">Our vision is to create an atmosphere that enables<br>inclusiveness of the whole community.</div>

  <p class="join" style="left:0;top:303px;width:396px;text-align:center">Come join us!</p>

  <svg class="scene" viewBox="0 0 690 418" aria-hidden="true">
    <path d="M463,0H690V418H629C478,400 384,318 384,190C384,110 416,46 463,0Z" fill="var(--sky)"/>
    <path d="M480,0H690V418H660C500,408 393,322 393,195C393,112 428,46 480,0Z" fill="var(--navy)"/>
  </svg>
  <svg class="scene" viewBox="0 0 690 418" role="img" aria-label="Photo of the studio interior: a bright chapel hall with yoga mats on a timber floor lit by stained-glass light">
    <defs>
      <linearGradient id="room2" x1="0" y1="0" x2="0" y2="1">
        <stop offset="0" stop-color="var(--photo-wall)"/>
        <stop offset=".5" stop-color="#b8a894"/>
        <stop offset=".62" stop-color="var(--photo-floor)"/>
        <stop offset=".85" stop-color="var(--photo-glow)"/>
        <stop offset="1" stop-color="#5a2a14"/>
      </linearGradient>
    </defs>
    <path d="M505,0H690V412C530,408 413,322 413,195C413,110 450,44 505,0Z" fill="url(#room2)"/>
  </svg>

  <div class="links">
    <svg class="links__globe" width="23" height="23" viewBox="0 0 24 24" aria-hidden="true"><g fill="none" stroke="var(--navy)" stroke-width="1.4"><circle cx="12" cy="12" r="10.5"/><ellipse cx="12" cy="12" rx="4.5" ry="10.5"/><path d="M1.5 12h21M3 6.5h18M3 17.5h18M12 1.5v21"/></g></svg>
    <span class="links__web">lanternreedyoga.com.au</span>
    <span class="social" style="left:206px"><span class="social__dot"></span>pagewell</span>
    <span class="social" style="left:268px"><span class="social__dot"></span>vibro</span>
    <span class="social" style="left:316px"><span class="social__dot"></span>calmora</span>
  </div>
  <div class="address">
    <svg width="12" height="17" viewBox="0 0 12 17" aria-hidden="true"><path d="M6 16C2 10.5 1 8.5 1 6a5 5 0 0 1 10 0c0 2.5-1 4.5-5 10z" fill="none" stroke="var(--white)" stroke-width="1.3"/></svg>
    The Chapel, 48 Harbour Lane Marrick NSW 2099
  </div>

  <svg class="scene" viewBox="0 0 690 418" role="img" aria-label="Photo of the chapel building exterior under a cloudy sky">
    <defs>
      <linearGradient id="chapel2" x1="0" y1="0" x2="0" y2="1">
        <stop offset="0" stop-color="#8fb4d6"/>
        <stop offset=".45" stop-color="#c9ccd0"/>
        <stop offset=".8" stop-color="#6d6a64"/>
        <stop offset="1" stop-color="#3c4a2e"/>
      </linearGradient>
    </defs>
    <circle cx="463" cy="341" r="67" fill="rgba(255,255,255,.35)"/>
    <circle cx="463" cy="341" r="60" fill="url(#chapel2)" stroke="var(--sky)" stroke-width="2.5"/>
  </svg>
</section>

</body>
</html>
```